Pelbrook Business Cards

Create new business cards with the details below.

Aaron Velst
Director

MB: +61 412 563 904
PH: 1300 417 639
Email: aaron.velst@pelbrook.com.au
Address: 27C Marlow Parade, Harrowdale VIC 3094 Australia
Website: www.pelbrook.com.au

Target Market(s)

Other business

Industry/Entity Type

Business

Requirements
Must have
• must be clean looking

```html
<!DOCTYPE html>
<html lang="en">
<head>
<meta charset="utf-8">
<title>Pelbrook Business Cards</title>
<link href="https://fonts.googleapis.com/css2?family=PT+Sans:ital,wght@0,400;0,700;1,400&family=Open+Sans:wght@400&display=swap" rel="stylesheet">
<style>
  :root {
    --page: #ffffff;
    --ink: #2a2d2e;
    --lime: #a6f00f;
    --card-line: #5a5a5a;
    --white: #ffffff;
  }
  html, body {
    margin: 0;
    padding: 0;
    width: 1200px;
    height: 1000px;
    overflow: hidden;
    background: var(--page);
  }
  .sheet {
    position: relative;
    width: 1200px;
    height: 1000px;
    font-family: "PT Sans", sans-serif;
    color: var(--ink);
  }
  .side-label {
    position: absolute;
    left: 141px;
    font-family: "Open Sans", sans-serif;
    font-size: 19px;
    color: #111;
    margin: 0;
  }
  .side-label--front { top: 42px; }
  .side-label--back { top: 528px; }

  .card {
    position: absolute;
    left: 247px;
    width: 743px;
    height: 438px;
    background: var(--white);
    border: 1px solid var(--card-line);
    box-sizing: border-box;
    box-shadow: 4px 5px 7px rgba(0,0,0,0.28);
  }
  .card--front { top: 45px; }
  .card--back { top: 529px; }

  .brand {
    position: absolute;
    display: flex;
    align-items: center;
  }
  .brand__mark {
    background: var(--lime);
    flex: none;
  }
  .brand__name {
    font-family: "PT Sans", sans-serif;
    font-weight: 700;
    color: var(--ink);
    line-height: 1;
    letter-spacing: 1px;
  }
  .card--front .brand { right: 46px; top: 46px; gap: 12px; }
  .card--front .brand__mark { width: 50px; height: 50px; }
  .card--front .brand__name { font-size: 50px; }

  .card--back .brand { left: 86px; top: 150px; gap: 20px; }
  .card--back .brand__mark { width: 88px; height: 88px; }
  .card--back .brand__name { font-size: 92px; letter-spacing: 3px; }

  .accent-bar {
    position: absolute;
    left: 45px;
    top: 152px;
  }

  .contact {
    position: absolute;
    left: 107px;
    top: 189px;
    margin: 0;
  }
  .contact__name {
    margin: 0;
    font-size: 34px;
    font-weight: 700;
    letter-spacing: 2.5px;
    line-height: 40px;
  }
  .contact__role {
    margin: 0 0 14px;
    font-size: 25px;
    font-style: italic;
    line-height: 32px;
  }
  .contact__list {
    list-style: none;
    margin: 0;
    padding: 0;
    font-size: 25px;
    line-height: 30px;
  }
  .contact__list li + li.contact__group { margin-top: 13px; }
  .contact__key { font-style: italic; }
  .contact__value--strong { font-weight: 700; }

  .address-band {
    position: absolute;
    left: 27px;
    top: 363px;
  }
  .address-band__text {
    position: absolute;
    left: 61px;
    top: 371px;
    width: 630px;
    margin: 0;
    font-size: 23px;
    letter-spacing: 2.4px;
    color: var(--white);
    line-height: 30px;
    white-space: nowrap;
  }
</style>
</head>
<body>
<main class="sheet">
  <p class="side-label side-label--front">Front</p>
  <section class="card card--front" aria-label="Business card front">
    <div class="brand">
      <span class="brand__mark"></span>
      <span class="brand__name">PELBROOK</span>
    </div>
    <svg class="accent-bar" width="44" height="253" viewBox="0 0 44 253" aria-hidden="true">
      <polygon points="0,0 43,31 43,253 0,221" fill="var(--lime)"/>
    </svg>
    <div class="contact">
      <h1 class="contact__name">AARON VELST</h1>
      <p class="contact__role">Director</p>
      <ul class="contact__list">
        <li><span class="contact__key">m:</span> <span class="contact__value--strong">+61 412 563 904</span></li>
        <li><span class="contact__key">p:</span> 1300 417 639</li>
        <li class="contact__group"><span class="contact__key">w:</span> <span class="contact__value--strong">www.pelbrook.com.au</span></li>
        <li><span class="contact__key">e:</span> aaron.velst@pelbrook.com.au</li>
      </ul>
    </div>
  </section>

  <p class="side-label side-label--back">Back</p>
  <section class="card card--back" aria-label="Business card back">
    <div class="brand">
      <span class="brand__mark"></span>
      <span class="brand__name">PELBROOK</span>
    </div>
    <svg class="address-band" width="697" height="48" viewBox="0 0 697 48" aria-hidden="true">
      <polygon points="0,47 23,0 696,0 673,47" fill="var(--ink)"/>
    </svg>
    <p class="address-band__text">27C Marlow Parade Harrowdale VIC 3094 Australia</p>
  </section>
</main>
</body>
</html>
```